Real eatate

My company name is “Maple Crest Realestate” i would like to create a business card. I would like something modern and sleek similar to picture uploaded. All text in the business card should be black and the logo gold any shade.

```html
<!DOCTYPE html>
<html lang="en">
<head>
<meta charset="utf-8">
<title>Maple Crest Realestate – Business Card</title>
<link href="https://fonts.googleapis.com/css2?family=Montserrat:wght@400;500;700&display=swap" rel="stylesheet">
<style>
  :root {
    --backdrop: #2b2b2d;
    --card: #707072;
    --ink: #000000;
    --gold: #d4ae3a;
    --emboss: #686869;
  }
  * { margin: 0; padding: 0; box-sizing: border-box; }
  html, body { width: 1200px; height: 888px; overflow: hidden; }
  body {
    background: var(--backdrop);
    font-family: "Montserrat", sans-serif;
    position: relative;
  }
  .card {
    position: absolute;
    width: 500px;
    height: 286px;
    background: var(--card);
    border-radius: 3px;
    box-shadow: 0 18px 40px rgba(0,0,0,0.45);
    overflow: hidden;
  }
  .card--front { left: 80px; top: 160px; }
  .card--back { left: 620px; top: 440px; }

  /* Front */
  .brand {
    position: absolute;
    inset: 0;
    display: flex;
    align-items: center;
    justify-content: center;
    gap: 14px;
  }
  .brand__mark {
    width: 24px; height: 24px;
    background: var(--gold);
    border-radius: 50%;
    flex: none;
  }
  .brand__name {
    color: var(--ink);
    font-weight: 700;
    font-size: 24px;
    letter-spacing: 1.5px;
    text-transform: uppercase;
    white-space: nowrap;
  }

  /* Back */
  .backdrop-name {
    position: absolute;
    left: 26px;
    bottom: 34px;
    color: var(--emboss);
    font-weight: 700;
    font-size: 46px;
    line-height: 1;
    text-transform: uppercase;
    letter-spacing: 1px;
  }
  .contact {
    position: absolute;
    right: 26px;
    top: 26px;
    text-align: right;
    font-size: 10px;
    line-height: 1.55;
    color: var(--ink);
  }
  .contact__name {
    font-weight: 700;
    font-size: 15px;
    letter-spacing: 0.8px;
    text-transform: uppercase;
    line-height: 1.2;
  }
  .contact__title { margin-bottom: 8px; }
  .contact__company { font-weight: 700; }
  .contact__address { margin-bottom: 8px; }
  .contact__list { list-style: none; }
  .contact__list li {
    display: flex;
    justify-content: flex-end;
    align-items: center;
    gap: 6px;
    white-space: nowrap;
  }
  .contact__list svg { width: 9px; height: 9px; fill: var(--ink); flex: none; }
</style>
</head>
<body>

<section class="card card--front" aria-label="Business card front">
  <div class="brand">
    <span class="brand__mark"></span>
    <span class="brand__name">Maple Crest Realestate</span>
  </div>
</section>

<section class="card card--back" aria-label="Business card back">
  <div class="backdrop-name" aria-hidden="true">Maple<br>Crest</div>
  <div class="contact">
    <p class="contact__name">Daniel Hayes</p>
    <p class="contact__title">President</p>
    <p class="contact__company">Maple Crest Realestate LLC</p>
    <p class="contact__address">4120 Birchwood Lane<br>Juneau, Alaska 99801</p>
    <ul class="contact__list">
      <li>555-214-7730
        <svg viewBox="0 0 10 10"><path d="M2 0.5 L3.6 2.6 L2.8 3.6 Q4 6 6.4 7.2 L7.4 6.4 L9.5 8 L8.4 9.5 Q3.5 9 0.5 1.6 Z"/></svg>
      </li>
      <li>555-318-4462
        <svg viewBox="0 0 10 10"><path d="M2.5 0 H7.5 V10 H2.5 Z M3.4 1 V8 H6.6 V1 Z" fill-rule="evenodd"/></svg>
      </li>
      <li>555-406-9185
        <svg viewBox="0 0 10 10"><path d="M2.5 0 H7.5 V3 H2.5 Z M0.5 3.5 H9.5 V8 H0.5 Z M2.5 7 H7.5 V10 H2.5 Z"/></svg>
      </li>
      <li>info@maplecrestrealty.com
        <svg viewBox="0 0 10 10"><path d="M0.5 2 H9.5 V8 H0.5 Z M1.2 2.6 L5 5.6 L8.8 2.6 Z" fill-rule="evenodd"/></svg>
      </li>
      <li>www.maplecrestrealty.com
        <svg viewBox="0 0 10 10"><circle cx="5" cy="5" r="4.5"/></svg>
      </li>
    </ul>
  </div>
</section>

</body>
</html>
```